Wills & Estate Planning *

I have my own logo, just looking for a nice eye catching background with good quality.

Could we find a place for 'We give you the peace of mind you deserve'
Updates

Could we find somewhere on the card to put 'We give you the peace of mind you deserve' Thanks.

Target Market(s)

40+ age

Industry/Entity Type

Law Firm

Contact Information for Business Card

Lionel Hartcombe
01632 960381
admin@galvinmerecourt.co.uk
www.galvinmerecourt.co.uk

Requirements
Must have
• Please use my logo attached on the brief

```html
<!DOCTYPE html>
<html lang="en">
<head>
<meta charset="utf-8">
<title>Galvin Merecourt – Business Card</title>
<link href="https://fonts.googleapis.com/css2?family=Lato:ital,wght@0,400;0,700;1,400&display=swap" rel="stylesheet">
<style>
  :root {
    --navy: #263f7a;
    --navy-deep: #1c3160;
    --navy-map: #3a5a9e;
    --grey-band: #8d8f9c;
    --paper: #f4f4f6;
    --ink: #2b2b33;
    --backdrop: #2a2a2c;
    --white: #ffffff;
    --white-soft: rgba(255,255,255,.82);
  }
  * { box-sizing: border-box; margin: 0; padding: 0; }
  html, body {
    width: 1200px; height: 997px; overflow: hidden;
    background: var(--backdrop);
    font-family: "Lato", Arial, sans-serif;
  }
  .stage { position: relative; width: 1200px; height: 997px; }

  .card {
    position: absolute;
    width: 560px; height: 320px;
    box-shadow: 0 18px 40px rgba(0,0,0,.55);
    overflow: hidden;
  }

  /* Front */
  .card-front {
    left: 80px; top: 110px;
    background: linear-gradient(160deg, var(--navy) 0%, var(--navy-deep) 100%);
  }
  .world-map {
    position: absolute; left: 30px; top: 20px; width: 500px; height: 270px;
    background:
      radial-gradient(ellipse 30% 38% at 28% 55%, rgba(58,90,158,.75) 0%, rgba(58,90,158,0) 100%),
      radial-gradient(ellipse 38% 34% at 66% 38%, rgba(58,90,158,.8) 0%, rgba(58,90,158,0) 100%),
      radial-gradient(ellipse 16% 22% at 52% 72%, rgba(58,90,158,.6) 0%, rgba(58,90,158,0) 100%),
      radial-gradient(ellipse 14% 14% at 84% 78%, rgba(58,90,158,.55) 0%, rgba(58,90,158,0) 100%);
  }
  .front-brand {
    position: absolute; left: 0; right: 0; top: 118px;
    text-align: center; color: var(--white);
    font-weight: 400; letter-spacing: 3px;
  }
  .front-brand .brand-name { font-size: 34px; line-height: 1.1; }
  .front-brand .brand-sub { font-size: 16px; letter-spacing: 2.5px; margin-top: 4px; }
  .brand-square {
    display: block; width: 26px; height: 26px; margin: 0 auto 14px;
    background: var(--white);
  }
  .tagline {
    position: absolute; left: 0; right: 0; bottom: 30px;
    text-align: center; color: var(--white-soft);
    font-size: 14px; font-style: italic; letter-spacing: .8px;
  }

  /* Back */
  .card-back {
    left: 560px; top: 560px;
    background: linear-gradient(135deg, var(--white) 0%, var(--paper) 100%);
  }
  .back-brand {
    position: absolute; left: 34px; top: 120px; width: 240px;
    color: var(--navy); font-weight: 400; letter-spacing: 1.5px;
  }
  .back-brand .brand-square { margin: 0 0 12px 0; background: var(--navy); width: 22px; height: 22px; }
  .back-brand .brand-name { font-size: 20px; line-height: 1.1; white-space: nowrap; }
  .back-brand .brand-sub { font-size: 11.5px; letter-spacing: 1.8px; margin-top: 5px; color: #5a5d6e; white-space: nowrap; }

  .divider {
    position: absolute; left: 282px; top: 54px; width: 2px; height: 150px;
    background: linear-gradient(to bottom, rgba(38,63,122,0), var(--navy) 45%, rgba(38,63,122,0));
  }

  .contact { position: absolute; left: 304px; top: 44px; color: var(--ink); }
  .person-name { font-size: 17px; color: var(--navy); letter-spacing: .5px; }
  .person-name strong { font-weight: 700; }
  .person-role { font-size: 12px; color: var(--ink); margin-top: 1px; }
  .website { font-size: 13px; font-weight: 700; color: var(--navy); margin-top: 24px; }
  .contact-list { list-style: none; margin-top: 18px; font-size: 13px; }
  .contact-list li { display: flex; align-items: center; gap: 10px; margin-bottom: 8px; }
  .contact-list svg { width: 13px; height: 13px; fill: var(--navy); flex: none; }

  .band { position: absolute; left: 0; bottom: 0; width: 100%; height: 74px; }
</style>
</head>
<body>
<main class="stage">

  <section class="card card-front" aria-label="Card front">
    <div class="world-map" role="img" aria-label="Faint dotted world map in lighter navy tones"></div>
    <div class="front-brand">
      <span class="brand-square"></span>
      <div class="brand-name">GALVIN MERECOURT</div>
      <div class="brand-sub">WILLS &amp; ESTATE PLANNING</div>
    </div>
    <p class="tagline">We give you the peace of mind you deserve</p>
  </section>

  <section class="card card-back" aria-label="Card back">
    <div class="back-brand">
      <span class="brand-square"></span>
      <div class="brand-name">GALVIN MERECOURT</div>
      <div class="brand-sub">WILLS &amp; ESTATE PLANNING</div>
    </div>

    <div class="divider"></div>

    <div class="contact">
      <p class="person-name">LIONEL <strong>HARTCOMBE</strong></p>
      <p class="person-role">Managing Director</p>
      <p class="website">www.galvinmerecourt.co.uk</p>
      <ul class="contact-list">
        <li>
          <svg viewBox="0 0 24 24" aria-hidden="true"><path d="M6.6 10.8a15.1 15.1 0 0 0 6.6 6.6l2.2-2.2a1 1 0 0 1 1-.25 11.4 11.4 0 0 0 3.6.57 1 1 0 0 1 1 1V20a1 1 0 0 1-1 1A17 17 0 0 1 3 4a1 1 0 0 1 1-1h3.5a1 1 0 0 1 1 1c0 1.25.2 2.45.57 3.57a1 1 0 0 1-.25 1z"/></svg>
          <span>01632 960381</span>
        </li>
        <li>
          <svg viewBox="0 0 24 24" aria-hidden="true"><path d="M2 5h20v14H2z"/><path d="M3.5 6.5 12 13l8.5-6.5" fill="none" stroke="#fff" stroke-width="1.6"/></svg>
          <span>admin@galvinmerecourt.co.uk</span>
        </li>
      </ul>
    </div>

    <svg class="band" viewBox="0 0 560 74" preserveAspectRatio="none" aria-hidden="true">
      <path d="M0 74 L0 58 L400 34 L560 24 L560 74 Z" fill="var(--navy)"/>
      <path d="M400 74 L400 50 Q404 20 440 18 L560 10 L560 74 Z" fill="var(--grey-band)"/>
    </svg>
  </section>

</main>
</body>
</html>
```